velmora - business cards

Need business card designs - logo provided - see www.velmora-example.co.nz

Industry/Entity Type

Business

Requirements
Must have
• logo - provided in attachments
• www.velmora-example.co.nz

```html
<!DOCTYPE html>
<html lang="en">
<head>
<meta charset="utf-8">
<title>velmora – business cards</title>
<link rel="stylesheet" href="https://fonts.googleapis.com/css2?family=Arimo:wght@400;700&family=Archivo+Black&family=Caveat:wght@600&display=swap">
<style>
  :root {
    --bg: #e9e6e1;
    --card-white: #f4f4f4;
    --card-grey: #dcdcdc;
    --ink: #4a4a4a;
    --ink-soft: #6b6b6b;
    --blue-mid: #2c5c98;
    --blue-light: #5c98cc;
    --orange-mid: #d9661f;
    --accent-orange: #f08a24;
    --divider: #bdbdbd;
  }
  * { box-sizing: border-box; margin: 0; padding: 0; }
  html, body { width: 1200px; height: 1000px; overflow: hidden; }
  body {
    background: var(--bg);
    font-family: "Arimo", Arial, sans-serif;
    color: var(--ink);
    position: relative;
  }
  .card {
    position: absolute;
    left: 290px;
    width: 620px;
    height: 354px;
    border-radius: 24px;
    overflow: hidden;
    background: linear-gradient(160deg, #ffffff 0%, var(--card-white) 50%, var(--card-grey) 100%);
    box-shadow: 0 10px 24px rgba(0,0,0,.18);
  }
  .card--front { top: 60px; }
  .card--back { top: 560px; }
  .card__band { position: absolute; inset: 0; width: 100%; height: 100%; }

  .brand {
    position: absolute;
    display: flex;
    align-items: center;
    gap: 12px;
    font-family: "Arimo", Arial, sans-serif;
    font-weight: 700;
    letter-spacing: -1px;
  }
  .brand__dot { width: 30px; height: 30px; border-radius: 50%; }
  .card--front .brand { left: 44px; top: 72px; font-size: 50px; color: var(--ink); }
  .card--front .brand__dot { background: var(--blue-light); }
  .card--back .brand { right: 40px; bottom: 40px; font-size: 42px; color: #ffffff; }
  .card--back .brand__dot { background: #ffffff; width: 26px; height: 26px; }

  .contact {
    position: absolute;
    border-left: 1px solid var(--divider);
    padding-left: 12px;
    list-style: none;
    font-size: 12px;
    line-height: 17px;
    color: var(--ink-soft);
  }
  .contact li { display: flex; align-items: flex-start; gap: 8px; }
  .contact svg { flex: none; margin-top: 3px; }
  .card--front .contact { left: 346px; top: 40px; }
  .card--back .contact { left: 376px; top: 48px; font-size: 13px; line-height: 19px; }

  .tagline {
    position: absolute;
    right: 34px;
    top: 216px;
    text-align: left;
    font-size: 14px;
    line-height: 19px;
    color: #ffffff;
  }
  .tagline__accent {
    font-family: "Caveat", cursive;
    font-weight: 600;
    font-size: 19px;
    color: var(--accent-orange);
  }

  .person { position: absolute; left: 40px; top: 60px; }
  .person__name {
    font-family: "Archivo Black", "Arial Black", sans-serif;
    font-size: 38px;
    letter-spacing: -1px;
    line-height: 1;
  }
  .person__first { color: var(--accent-orange); }
  .person__last { color: var(--ink); }
  .person__role {
    font-size: 13px;
    color: var(--ink-soft);
    margin-top: 4px;
    text-align: right;
  }
</style>
</head>
<body>

<section class="card card--front" aria-label="Business card front">
  <svg class="card__band" viewBox="0 0 620 354" preserveAspectRatio="none" aria-hidden="true">
    <defs>
      <linearGradient id="blueBand" x1="0" y1="1" x2="1" y2="0">
        <stop offset="0" stop-color="#3b78b8"/>
        <stop offset="0.45" stop-color="#2c5c98"/>
        <stop offset="1" stop-color="#14284a"/>
      </linearGradient>
      <linearGradient id="blueSheen" x1="0" y1="0" x2="1" y2="0">
        <stop offset="0" stop-color="#8fc0e8" stop-opacity=".45"/>
        <stop offset="1" stop-color="#8fc0e8" stop-opacity="0"/>
      </linearGradient>
    </defs>
    <path d="M0 354 L0 300 C160 270 330 230 620 150 L620 354 Z" fill="url(#blueBand)"/>
    <path d="M0 330 C180 300 360 255 620 190 L620 230 C380 285 190 325 0 354 Z" fill="url(#blueSheen)"/>
  </svg>

  <div class="brand"><span class="brand__dot"></span>velmora</div>

  <ul class="contact">
    <li>
      <svg width="9" height="9" viewBox="0 0 10 10"><path d="M2 0 L4 2 L3 3.5 Q4.5 6 6.5 7 L8 6 L10 8 L8.5 10 Q2 9 0 1.5 Z" fill="var(--blue-mid)"/></svg>
      <span>0800 2 VELMO (0800 28 35 66)</span>
    </li>
    <li>
      <svg width="9" height="9" viewBox="0 0 10 10"><path d="M5 0 A3.5 3.5 0 0 1 8.5 3.5 C8.5 6 5 10 5 10 C5 10 1.5 6 1.5 3.5 A3.5 3.5 0 0 1 5 0 Z" fill="var(--blue-mid)"/><circle cx="5" cy="3.5" r="1.3" fill="#fff"/></svg>
      <span>P.O.Box 482210, Auckland,<br>0614, New Zealand</span>
    </li>
    <li>
      <svg width="9" height="9" viewBox="0 0 10 10"><rect x="0" y="2" width="10" height="7" fill="var(--blue-mid)"/><path d="M0 2 L5 6 L10 2" stroke="#fff" fill="none"/></svg>
      <span>info@velmora-example.co.nz</span>
    </li>
    <li>
      <svg width="9" height="9" viewBox="0 0 10 10"><circle cx="5" cy="5" r="4.5" fill="var(--blue-mid)"/><path d="M0.5 5 H9.5 M5 0.5 V9.5" stroke="#fff" stroke-width=".8"/></svg>
      <span>www.velmora-example.co.nz</span>
    </li>
  </ul>

  <p class="tagline">Build <span class="tagline__accent">clear online booking tools</span><br>teams enjoy every day.</p>
</section>

<section class="card card--back" aria-label="Business card back">
  <svg class="card__band" viewBox="0 0 620 354" preserveAspectRatio="none" aria-hidden="true">
    <defs>
      <linearGradient id="orangeBand" x1="0" y1="1" x2="1" y2="0">
        <stop offset="0" stop-color="#f2a23e"/>
        <stop offset="0.5" stop-color="#d9661f"/>
        <stop offset="1" stop-color="#b5461a"/>
      </linearGradient>
      <linearGradient id="orangeSheen" x1="0" y1="0" x2="1" y2="0">
        <stop offset="0" stop-color="#ffd08a" stop-opacity=".4"/>
        <stop offset="1" stop-color="#ffd08a" stop-opacity="0"/>
      </linearGradient>
    </defs>
    <path d="M0 354 L0 300 C160 270 330 230 620 150 L620 354 Z" fill="url(#orangeBand)"/>
    <path d="M0 330 C180 300 360 255 620 190 L620 230 C380 285 190 325 0 354 Z" fill="url(#orangeSheen)"/>
  </svg>

  <div class="person">
    <p class="person__name"><span class="person__first">MARLA</span><span class="person__last">QUINN</span></p>
    <p class="person__role">Vice President</p>
  </div>

  <ul class="contact">
    <li>
      <svg width="10" height="10" viewBox="0 0 10 10"><path d="M2 0 L4 2 L3 3.5 Q4.5 6 6.5 7 L8 6 L10 8 L8.5 10 Q2 9 0 1.5 Z" fill="var(--orange-mid)"/></svg>
      <span>+64 21 555 0142</span>
    </li>
    <li>
      <svg width="10" height="10" viewBox="0 0 10 10"><rect x="0" y="3" width="10" height="7" rx="1" fill="var(--orange-mid)"/><rect x="3" y="0.5" width="4" height="3" fill="none" stroke="var(--orange-mid)"/></svg>
      <span>+64 21 555 0143</span>
    </li>
    <li>
      <svg width="10" height="10" viewBox="0 0 10 10"><rect x="0" y="2" width="10" height="7" fill="var(--orange-mid)"/><path d="M0 2 L5 6 L10 2" stroke="#fff" fill="none"/></svg>
      <span>marla@velmora-example.co.nz</span>
    </li>
  </ul>

  <div class="brand"><span class="brand__dot"></span>velmora</div>
</section>

</body>
</html>
```